Website design for recruitment solutions

We connect top talents to fast growing employers in Asia. We need to revamp our existing website (currently outdated) and also add more pages to make it more informative for talents and employers.
We need final design output to be for both desktop and mobile devices. The final design output must come with all specifications so it's easier for our dev team to implement. We have a detailed mockup but we expect the design to be significantly changed by the final output. We want the pages to look aesthetic, modern and professional.
Number of Pages Required
5+ page
Requirements
Must have
- - To have Pages design for desktop+mobile. Need to take into account intermediate resolutions like 1365px\1023px\767px\479px, especially if mobile/desktop design differs considerably. Design should be repeatable (between pages), suitable for block-layout.
Nice to have
- In terms of receiving files, we usually work with designers who can deliver files in Figma or Sketch with export to Figma. If in PSD format - please export to Zeplin or Avocode, otherwise will be difficult to open

```html
<!DOCTYPE html>
<html lang="en">
<head>
<meta charset="utf-8">
<title>Tallora Recruitment – Home</title>
<link href="https://fonts.googleapis.com/css2?family=Figtree:wght@300;400;500;600&display=swap" rel="stylesheet">
<style>
:root{
  --backdrop:#efeae5;
  --white:#ffffff;
  --ink:#2b2b2b;
  --muted:#6b6b6b;
  --line:#e6e6e6;
  --red:#ff0000;
  --blue:#1e86cc;
  --blue-bright:#1f8fe0;
  --halo:#f6f1ee;
  --footer:#3d3d3d;
  --footer-text:#d9d9d9;
  --star-soft:#f07c7c;
}
*{box-sizing:border-box;margin:0;padding:0}
html,body{width:1200px;height:1200px;overflow:hidden}
body{background:var(--backdrop);font-family:"Figtree",Arial,sans-serif;color:var(--ink);position:relative}
.page{position:absolute;left:379.5px;top:50px;width:710px;height:1772px;background:var(--white);transform:scale(0.6211);transform-origin:0 0;overflow:hidden}
.abs{position:absolute}
.photo{position:absolute;border-radius:50%;background:radial-gradient(circle at 50% 38%,#c9b8a8 0,#8a7b70 45%,#4b4f57 100%)}

/* nav */
.nav{position:absolute;left:0;top:0;width:710px;height:42px;border-bottom:1px solid var(--line)}
.brand{position:absolute;left:27px;top:8px}
.brand-name{font-size:19px;font-weight:500;letter-spacing:.2px;line-height:20px;color:var(--ink)}
.brand-sub{font-size:4.5px;letter-spacing:3px;color:var(--muted);margin-top:1px}
.nav-link{position:absolute;top:16px;font-size:8px;color:var(--muted)}
.nav-link.active{color:var(--ink)}
.nav-link.active::after{content:"";position:absolute;left:0;right:0;bottom:-5px;height:1.5px;background:var(--red)}
.btn-outline{position:absolute;left:557px;top:9px;width:57px;height:24px;border:1px solid var(--blue);color:var(--blue);font-size:8px;display:flex;align-items:center;justify-content:center}
.btn-red{position:absolute;left:621px;top:9px;width:57px;height:24px;background:var(--red);color:var(--white);font-size:8px;display:flex;align-items:center;justify-content:center}

/* hero */
.hero-title{position:absolute;left:28px;top:137px;font-size:20px;font-weight:300;line-height:26px;color:var(--ink)}
.hero-text{position:absolute;left:28px;top:199px;width:215px;font-size:7px;line-height:10.5px;color:var(--muted)}
.cta{position:absolute;left:28px;top:235px;width:94px;height:29px;background:var(--red);color:var(--white);font-size:8px;display:flex;align-items:center;justify-content:center;gap:6px}
.orbit{position:absolute;left:0;top:0;width:710px;height:480px}
.halo{position:absolute;left:421px;top:137px;width:150px;height:150px;border-radius:50%;background:var(--halo)}
.scroll-hint{position:absolute;left:22px;top:378px}

/* smart connections */
.card{position:absolute;background:var(--white);box-shadow:0 1px 5px rgba(0,0,0,.12)}
.card-name{position:absolute;left:11px;font-size:8px;font-weight:600}
.card-role{position:absolute;left:11px;width:100px;font-size:6px;line-height:8.5px;color:var(--muted)}
.skill{position:absolute;left:11px;font-size:5.5px;color:var(--muted)}
.tick{position:absolute;right:8px;width:7px;height:7px}
.match-bar{position:absolute;background:var(--blue-bright);color:var(--white);font-size:8px;display:flex;align-items:center;padding-left:11px}
.section-title{font-size:15px;font-weight:400;color:var(--ink)}
.section-text{font-size:7px;line-height:10.5px;color:var(--muted)}

/* insights */
.insights{position:absolute;left:0;top:771px;width:710px;height:292px}
.insights-panel{position:absolute;left:0;top:0;width:355px;height:292px;background:var(--blue)}
.insights-photo{position:absolute;left:355px;top:0;width:355px;height:292px;background:linear-gradient(100deg,#d8d5d0 0,#7e7770 30%,#595652 48%,#c9d0d6 70%,#e9ecee 100%)}
.btn-white{position:absolute;left:52px;top:174px;width:94px;height:29px;background:var(--white);color:var(--blue);font-size:8px;display:flex;align-items:center;justify-content:center;gap:6px}
.mini{position:absolute;background:var(--white);box-shadow:0 1px 4px rgba(0,0,0,.15)}

/* testimonials */
.quote-card{position:absolute;top:1211px;width:149px;height:226px;background:var(--white);box-shadow:0 1px 5px rgba(0,0,0,.12)}
.quote-card .photo{left:44.5px;top:16px;width:60px;height:60px}
.q-name{position:absolute;left:13px;top:93px;font-size:8px;font-weight:600}
.q-role{position:absolute;left:13px;top:110px;font-size:6px;color:var(--muted)}
.q-text{position:absolute;left:13px;top:126px;width:125px;font-size:5.8px;line-height:8.8px;color:var(--muted)}
.stars{position:absolute;left:13px;top:195px}

/* footer */
.footer{position:absolute;left:0;top:1539px;width:710px;height:233px;background:var(--footer);color:var(--footer-text)}
.f-head{position:absolute;top:35px;font-size:9px;padding-bottom:6px;border-bottom:1px solid #565656}
.f-link{position:absolute;font-size:8px}
.f-text{position:absolute;left:26px;top:66px;width:188px;font-size:6.6px;line-height:10.3px}
.f-pill{position:absolute;left:290px;top:113px;width:62px;height:23px;border-radius:12px;background:var(--red);color:var(--white);font-size:8px;display:flex;align-items:center;justify-content:center}
.f-social{position:absolute;top:150px;width:11px;height:11px;background:var(--footer-text);border-radius:2px}
.f-rule{position:absolute;left:26px;top:184px;width:654px;height:1px;background:#565656}
.f-small{position:absolute;top:198px;font-size:5.5px}
</style>
</head>
<body>
<div class="page">

  <header class="nav">
    <div class="brand"><div class="brand-name">Tallora</div><div class="brand-sub">Recruitment</div></div>
    <span class="nav-link active" style="left:314px">How we work</span>
    <span class="nav-link" style="left:384px">Browse jobs</span>
    <span class="nav-link" style="left:449px">Employers</span>
    <span class="nav-link" style="left:507px">About us</span>
    <span class="btn-outline">Log In</span>
    <span class="btn-red">Register</span>
  </header>

  <section class="hero">
    <svg class="orbit" viewBox="0 0 710 480">
      <circle cx="488" cy="228" r="222" fill="none" stroke="#9a9a9a" stroke-width=".8" stroke-dasharray="1.5 3"/>
      <circle cx="497" cy="212" r="134" fill="none" stroke="#9a9a9a" stroke-width=".8" stroke-dasharray="1.5 3"/>
    </svg>
    <div class="halo"></div>
    <div class="photo" role="img" aria-label="Portrait of a candidate with glasses" style="left:444px;top:160px;width:104px;height:104px;background:radial-gradient(circle at 50% 40%,#b99a84 0,#6d7a86 55%,#3f5566 100%)"></div>
    <div class="photo" role="img" aria-label="Candidate portrait" style="left:289px;top:61px;width:42px;height:42px;background:radial-gradient(circle,#d8c7b4,#9a928c)"></div>
    <div class="photo" role="img" aria-label="Candidate portrait" style="left:419px;top:68px;width:44px;height:44px;background:radial-gradient(circle,#8d8a80,#3a3f3a)"></div>
    <div class="photo" role="img" aria-label="Candidate portrait" style="left:588px;top:126px;width:42px;height:42px;background:radial-gradient(circle,#e5d3c2,#a68d78)"></div>
    <div class="photo" role="img" aria-label="Candidate portrait" style="left:343px;top:234px;width:52px;height:52px;background:radial-gradient(circle,#9a8f82,#2f3236)"></div>
    <div class="photo" role="img" aria-label="Candidate portrait" style="left:540px;top:282px;width:64px;height:64px;background:radial-gradient(circle,#b07a5d,#1f2230)"></div>
    <div class="photo" role="img" aria-label="Candidate portrait" style="left:287px;top:331px;width:30px;height:30px;background:radial-gradient(circle,#a9a39a,#3e4246)"></div>

    <h1 class="hero-title">We connect top talent with<br>fast growing employers in Asia.</h1>
    <p class="hero-text">It’s the quality of the connection that matters. Our role matching algorithms and talent managers work around.</p>
    <span class="cta">Get Started
      <svg width="5" height="8" viewBox="0 0 5 8"><path d="M1 1l3 3-3 3" fill="none" stroke="#fff" stroke-width="1.2"/></svg></span>
    <svg class="scroll-hint" width="16" height="16" viewBox="0 0 16 16"><circle cx="8" cy="8" r="7.5" fill="#fff"/><path d="M4.5 6.5l3.5 3.5 3.5-3.5" fill="none" stroke="#333" stroke-width="1"/></svg>
  </section>

  <section class="smart">
    <svg class="abs" style="left:0;top:640px" width="320" height="80" viewBox="0 0 320 80">
      <path d="M97 12 Q130 62 186 60 Q232 58 258 32" fill="none" stroke="#1f8fe0" stroke-width=".8" stroke-dasharray="1.2 2.5"/>
      <circle cx="186" cy="60" r="8" fill="#fff"/>
      <path d="M184 56l4 4-4 4" fill="none" stroke="#1f8fe0" stroke-width="1"/>
    </svg>

    <div class="card" style="left:62px;top:466px;width:120px;height:186px">
      <div class="photo" role="img" aria-label="Portrait of Daniel Lowe" style="left:38px;top:12px;width:50px;height:50px;background:radial-gradient(circle at 50% 40%,#b99a84,#4f6474)"></div>
      <span class="card-name" style="top:74px">Daniel Lowe</span>
      <span class="card-role" style="top:89px">Senior product designer based in California</span>
      <span class="skill" style="top:116px">User Interface Design</span>
      <span class="skill" style="top:129px">Prototyping</span>
      <span class="skill" style="top:141px">Product Design</span>
      <span class="skill" style="top:153px">3D Design</span>
      <span class="skill" style="top:165px">Product Development</span>
    </div>

    <div class="card" style="left:193px;top:466px;width:120px;height:186px">
      <div class="photo" role="img" aria-label="Portrait of Karen Lim" style="left:38px;top:12px;width:50px;height:50px;background:radial-gradient(circle at 50% 40%,#9a8f80,#2f3432)"></div>
      <span class="card-name" style="top:74px">Karen Lim</span>
      <span class="card-role" style="top:89px">Head of product at Brightway based in Shanghai</span>
      <span class="skill" style="top:116px">Match</span>
      <span class="skill" style="top:129px">Match</span>
      <span class="skill" style="top:141px">Match</span>
      <span class="skill" style="top:153px">Match</span>
      <span class="skill" style="top:165px">Match</span>
      <svg class="tick" style="top:116px" viewBox="0 0 8 8"><circle cx="4" cy="4" r="3.6" fill="none" stroke="#cfe3f3" stroke-width=".6"/><path d="M2.2 4.2l1.3 1.2 2.4-2.8" fill="none" stroke="#1f8fe0" stroke-width=".8"/></svg>
      <svg class="tick" style="top:128px" viewBox="0 0 8 8"><circle cx="4" cy="4" r="3.6" fill="none" stroke="#cfe3f3" stroke-width=".6"/><path d="M2.2 4.2l1.3 1.2 2.4-2.8" fill="none" stroke="#1f8fe0" stroke-width=".8"/></svg>
      <svg class="tick" style="top:140px" viewBox="0 0 8 8"><circle cx="4" cy="4" r="3.6" fill="none" stroke="#cfe3f3" stroke-width=".6"/><path d="M2.2 4.2l1.3 1.2 2.4-2.8" fill="none" stroke="#1f8fe0" stroke-width=".8"/></svg>
      <svg class="tick" style="top:152px" viewBox="0 0 8 8"><circle cx="4" cy="4" r="3.6" fill="none" stroke="#cfe3f3" stroke-width=".6"/><path d="M2.2 4.2l1.3 1.2 2.4-2.8" fill="none" stroke="#1f8fe0" stroke-width=".8"/></svg>
      <svg class="tick" style="top:164px" viewBox="0 0 8 8"><circle cx="4" cy="4" r="3.6" fill="none" stroke="#cfe3f3" stroke-width=".6"/><path d="M2.2 4.2l1.3 1.2 2.4-2.8" fill="none" stroke="#1f8fe0" stroke-width=".8"/></svg>
    </div>
    <div class="match-bar" style="left:193px;top:649px;width:120px;height:24px">Profile Match
      <svg class="abs" style="right:4px;top:4px" width="16" height="16" viewBox="0 0 16 16"><circle cx="8" cy="8" r="7.5" fill="#fff"/><path d="M4.5 8.3l2.4 2.3 4.6-5" fill="none" stroke="#1f8fe0" stroke-width="1.2"/></svg>
    </div>

    <h2 class="section-title abs" style="left:425px;top:527px">Smart connections</h2>
    <p class="section-text abs" style="left:425px;top:557px;width:195px">It’s the quality of the connection that matters. Our role matching algorithms and talent managers work around the clock to find opportunities suitable to your unique profile.</p>
  </section>

  <section class="insights">
    <div class="insights-panel">
      <h2 class="section-title abs" style="left:54px;top:78px;color:#fff">Critical insights</h2>
      <p class="section-text abs" style="left:54px;top:110px;width:225px;color:#e6f1fa">Our close interactions with candidates and employers have helped us create a comprehensive database of companies, talents and skills. With TALLORA, you will gain full access to timely intel to help you make the right career decision.</p>
      <span class="btn-white">Find out more
        <svg width="5" height="8" viewBox="0 0 5 8"><path d="M1 1l3 3-3 3" fill="none" stroke="#1e86cc" stroke-width="1.2"/></svg></span>
    </div>
    <div class="insights-photo" role="img" aria-label="Photo of a young man with glasses working at a computer in a bright office"></div>

    <div class="mini" style="left:533px;top:25px;width:130px;height:38px">
      <div class="photo" role="img" aria-label="Recruiter portrait" style="left:10px;top:6px;width:26px;height:26px;background:radial-gradient(circle,#9a8f80,#2f3432)"></div>
      <span class="abs" style="left:44px;top:10px;font-size:6.3px;line-height:8.5px;color:#333">Looking for a senior<br>product designer</span>
    </div>
    <div class="abs" style="left:533px;top:74px;width:119px;height:22px;background:var(--red);color:#fff;font-size:7.5px;padding:6px 0 0 10px">Registered users
      <svg class="abs" style="right:4px;top:3px" width="16" height="16" viewBox="0 0 16 16"><circle cx="8" cy="8" r="7.5" fill="#fff"/><circle cx="8" cy="6.3" r="2.2" fill="#f00"/><path d="M4.3 12a3.8 3.2 0 017.4 0z" fill="#f00"/></svg>
    </div>
    <div class="mini" style="left:670px;top:107px;width:50px;height:130px;opacity:.75">
      <div class="photo" role="img" aria-label="Candidate portrait" style="left:6px;top:6px;width:22px;height:22px;background:radial-gradient(circle,#b99a84,#4f6474)"></div>
      <span class="skill" style="left:4px;top:46px">User Interface</span>
      <span class="skill" style="left:4px;top:58px">Prototyping</span>
      <span class="skill" style="left:4px;top:70px">Product Design</span>
      <span class="skill" style="left:4px;top:82px">3D Design</span>
      <span class="skill" style="left:4px;top:94px">Product Devel.</span>
    </div>
    <div class="mini" style="left:535px;top:104px;width:118px;height:137px">
      <div class="photo" role="img" aria-label="Portrait of Daniel Lowe" style="left:7px;top:7px;width:26px;height:26px;background:radial-gradient(circle,#b99a84,#4f6474)"></div>
      <span class="abs" style="left:43px;top:9px;font-size:7px;font-weight:600">Daniel Lowe</span>
      <span class="abs" style="left:43px;top:19px;font-size:5.8px;color:#666">Sn Product Designer</span>
      <span class="skill" style="left:10px;top:47px;font-size:5px">User Interface Design</span>
      <span class="skill" style="left:10px;top:59px;font-size:5px">Prototyping</span>
      <span class="skill" style="left:10px;top:71px;font-size:5px">Product Design</span>
      <span class="skill" style="left:10px;top:83px;font-size:5px">3D Design</span>
      <span class="skill" style="left:10px;top:95px;font-size:5px">Product Development</span>
      <svg class="tick" style="top:48px" viewBox="0 0 8 8"><path d="M2.2 4.2l1.3 1.2 2.4-2.8" fill="none" stroke="#1f8fe0" stroke-width=".8"/></svg>
      <svg class="tick" style="top:60px" viewBox="0 0 8 8"><path d="M2.2 4.2l1.3 1.2 2.4-2.8" fill="none" stroke="#1f8fe0" stroke-width=".8"/></svg>
      <svg class="tick" style="top:72px" viewBox="0 0 8 8"><path d="M2.2 4.2l1.3 1.2 2.4-2.8" fill="none" stroke="#1f8fe0" stroke-width=".8"/></svg>
      <svg class="tick" style="top:84px" viewBox="0 0 8 8"><path d="M2.2 4.2l1.3 1.2 2.4-2.8" fill="none" stroke="#1f8fe0" stroke-width=".8"/></svg>
      <svg class="tick" style="top:96px" viewBox="0 0 8 8"><path d="M2.2 4.2l1.3 1.2 2.4-2.8" fill="none" stroke="#1f8fe0" stroke-width=".8"/></svg>
      <div class="match-bar" style="left:0;top:112px;width:118px;height:25px;font-size:6.8px">Profile Match
        <svg class="abs" style="right:24px;top:5px" width="15" height="15" viewBox="0 0 16 16"><circle cx="8" cy="8" r="7.5" fill="#fff"/><rect x="4" y="5" width="8" height="6" rx=".6" fill="none" stroke="#1f8fe0" stroke-width="1"/><path d="M4 5.3l4 3 4-3" fill="none" stroke="#1f8fe0" stroke-width="1"/></svg>
        <svg class="abs" style="right:5px;top:5px" width="15" height="15" viewBox="0 0 16 16"><circle cx="8" cy="8" r="7.5" fill="#fff"/><path d="M5.5 4.5l1.6 2-1 1.2a5 5 0 002.2 2.2l1.2-1 2 1.6-1 1.5c-3 0-6.5-3.5-6.5-6.5z" fill="#1f8fe0"/></svg>
      </div>
    </div>
    <svg class="abs" style="left:644px;top:250px" width="28" height="8" viewBox="0 0 28 8"><circle cx="4" cy="4" r="2.2" fill="#fff"/><circle cx="13" cy="4" r="2" fill="none" stroke="#fff" stroke-width=".7"/><circle cx="22" cy="4" r="2" fill="none" stroke="#fff" stroke-width=".7"/></svg>
  </section>

  <section class="people">
    <h2 class="section-title abs" style="left:0;width:710px;text-align:center;top:1111px">People first</h2>
    <p class="section-text abs" style="left:215px;width:280px;text-align:center;top:1143px">We take the time to really understand you holistically as a person to maximize your potential. As your career counselor, we provide maximum transparency and feedback throughout the process.</p>

    <svg class="abs" style="left:190px;top:1430px" width="330" height="80" viewBox="0 0 330 80">
      <path d="M18 8 Q165 130 312 8" fill="none" stroke="#9a9a9a" stroke-width=".8" stroke-dasharray="1.5 3"/>
    </svg>

    <article class="quote-card" style="left:109px">
      <div class="photo" role="img" aria-label="Portrait of Lena Chow" style="background:radial-gradient(circle at 50% 40%,#d6b7a0,#3d2a25)"></div>
      <span class="q-name">Lena Chow</span><span class="q-role">Robotic engineer</span>
      <p class="q-text">“Tallora guided me through every part of the process, they used my profile to connect me with some of the top people in my industry. So glad I registered with Tallora as they kept giving me job updates”</p>
      <svg class="stars" width="80" height="12" viewBox="0 0 80 12"><g fill="#f00"><path id="st" d="M6 0.5l1.6 3.6 3.9.4-2.9 2.6.8 3.9L6 9l-3.4 2 .8-3.9L.5 4.5l3.9-.4z"/><use href="#st" x="16"/><use href="#st" x="32"/><use href="#st" x="48"/></g><use href="#st" x="64" fill="#f07c7c"/></svg>
    </article>

    <article class="quote-card" style="left:280px">
      <div class="photo" role="img" aria-label="Portrait of Yuri Tan" style="background:radial-gradient(circle at 50% 40%,#c7a995,#4a4e5a)"></div>
      <span class="q-name">Yuri Tan</span><span class="q-role">Senior software engineer</span>
      <p class="q-text">“Tallora took my job experience and managed to match me with my dream job. They were helpful every step of the way from interview advice to putting me in contact with leading companies in my field”</p>
      <svg class="stars" width="80" height="12" viewBox="0 0 80 12"><g fill="#f00"><use href="#st"/><use href="#st" x="16"/><use href="#st" x="32"/><use href="#st" x="48"/><use href="#st" x="64"/></g></svg>
    </article>

    <article class="quote-card" style="left:451px">
      <div class="photo" role="img" aria-label="Portrait of Ryan Hale" style="background:radial-gradient(circle at 50% 40%,#d8b9a2,#6f7474)"></div>
      <span class="q-name">Ryan Hale</span><span class="q-role">Product technologist</span>
      <p class="q-text">“Setting up my application was extremely easy, their algorithm matched me some top clients instantly. The talent managers also help with the interview process and got me into a fantastic new job”</p>
      <svg class="stars" width="80" height="12" viewBox="0 0 80 12"><g fill="#f00"><use href="#st"/><use href="#st" x="16"/><use href="#st" x="32"/><use href="#st" x="48"/></g><use href="#st" x="64" fill="#f07c7c"/></svg>
    </article>

    <svg class="abs" style="left:335px;top:1461px" width="40" height="12" viewBox="0 0 40 12"><circle cx="6" cy="6" r="3" fill="#333"/><circle cx="20" cy="6" r="2.7" fill="none" stroke="#333" stroke-width=".8"/><circle cx="33" cy="6" r="2.7" fill="none" stroke="#333" stroke-width=".8"/></svg>
  </section>

  <footer class="footer">
    <span class="f-head" style="left:26px;width:200px">Tallora</span>
    <span class="f-head" style="left:290px;width:112px">Talents</span>
    <span class="f-head" style="left:426px;width:112px">Employers</span>
    <span class="f-head" style="left:563px;width:112px">About us</span>
    <p class="f-text">TALLORA is a modern recruitment partner for high potential technology and finance talents. We work closely with hedge funds, systematic trading and FinTech employers experiencing hyper growth in Asia.</p>
    <span class="f-link" style="left:290px;top:68px">How we work</span>
    <span class="f-link" style="left:290px;top:89px">Browse jobs</span>
    <span class="f-pill">Register</span>
    <span class="f-link" style="left:426px;top:68px">Why TALLORA</span>
    <span class="f-link" style="left:563px;top:68px">About TALLORA</span>
    <span class="f-link" style="left:563px;top:89px">Working at TALLORA</span>
    <span class="f-social" style="left:26px"></span>
    <span class="f-social" style="left:48px;border-radius:50%"></span>
    <div class="f-rule"></div>
    <span class="f-small" style="left:26px">Tallora 2012-2020. All rights reserved.</span>
    <span class="f-small" style="right:30px">Privacy Policy &nbsp;I User Agreement</span>
  </footer>

</div>
</body>
</html>
```